CRPG is needing business cards, and stationary created.

Pixel Forge created a logo for our business, and now we are wanting business cards, and stationary. I have included two designs of the same logo. Please feel free to use them as you want. The name of the company is Cedar Ridge Property Group LLC, the address is 812 NE Willow Ln., Suite 9, the city & state is Bend, Oregon, zip code is 97815, Telephone number is 541-327-4489, Fax number is 541-327-6051, the name on the business card is Carl Whitby CMCA

Industry/Entity Type

Property Management

Contact Information for Business Card

The card needs to look professional. Upscale.

Requirements
Must have
• The colors we are using are on the logo that has been uploaded.

```html
<!DOCTYPE html>
<html lang="en">
<head>
<meta charset="utf-8">
<title>Cedar Ridge Property Group – Business Cards</title>
<link rel="stylesheet" href="https://fonts.googleapis.com/css2?family=Montserrat:wght@800&family=Roboto:wght@400;500&display=swap">
<style>
  :root {
    --teal: #1b907c;
    --teal-dark: #157565;
    --slate: #3e4a5b;
    --slate-dark: #2a3340;
    --white: #ffffff;
    --ink: #1d1d1d;
    --backdrop: #2a2a2a;
  }
  * { margin: 0; padding: 0; box-sizing: border-box; }
  html, body { width: 1200px; height: 900px; overflow: hidden; }
  body {
    background: var(--backdrop);
    position: relative;
    font-family: "Roboto", Arial, sans-serif;
  }
  .card {
    position: absolute;
    width: 700px;
    height: 400px;
    border-radius: 22px;
    overflow: hidden;
    box-shadow: 0 14px 30px rgba(0,0,0,0.55);
  }
  .card-front { left: 120px; top: 40px; background: var(--teal); }
  .card-back  { left: 380px; top: 470px; background: var(--white); }

  .wordmark {
    display: flex;
    align-items: center;
    gap: 18px;
    font-family: "Montserrat", Arial, sans-serif;
    font-weight: 800;
    letter-spacing: 1px;
    white-space: nowrap;
  }
  .wordmark-square { display: block; flex: none; }
  .card-front .wordmark {
    position: absolute; left: 0; right: 0; top: 160px;
    justify-content: center;
    color: var(--white); font-size: 58px;
  }
  .card-front .wordmark-square { width: 56px; height: 56px; background: var(--white); }

  .back-shapes { position: absolute; inset: 0; }

  .card-back .wordmark {
    position: absolute; left: 40px; top: 70px; width: 250px;
    flex-direction: column; gap: 10px;
    color: var(--teal); font-size: 27px;
  }
  .card-back .wordmark-square { width: 34px; height: 34px; background: var(--slate); }

  .name-ribbon {
    position: absolute; left: 300px; top: 46px; width: 360px; height: 62px;
    color: var(--white); text-align: center; padding-top: 10px;
  }
  .person-name { font-size: 22px; font-weight: 500; }
  .person-title { font-size: 11px; letter-spacing: 0.5px; margin-top: 2px; }

  .contact-list {
    position: absolute; left: 40px; top: 236px;
    list-style: none; color: var(--ink); font-size: 17px;
  }
  .contact-list li { display: flex; align-items: center; gap: 12px; height: 32px; white-space: nowrap; }
  .contact-icon { width: 24px; height: 24px; flex: none; }

  .address {
    position: absolute; right: 30px; bottom: 70px; width: 240px;
    color: var(--white); font-size: 15px; line-height: 1.35; text-align: center;
  }
  .address svg { display: block; margin: 0 auto 6px; }
</style>
</head>
<body>

<section class="card card-front" aria-label="Business card front">
  <div class="wordmark"><span class="wordmark-square"></span>CEDAR RIDGE</div>
</section>

<section class="card card-back" aria-label="Business card back">
  <svg class="back-shapes" width="700" height="400" viewBox="0 0 700 400">
    <defs>
      <filter id="panel-shadow" x="-10%" y="-10%" width="120%" height="120%">
        <feDropShadow dx="-6" dy="0" stdDeviation="6" flood-color="#000" flood-opacity="0.3"/>
      </filter>
    </defs>
    <polygon points="330,0 700,0 700,400 410,400" fill="var(--teal)" filter="url(#panel-shadow)"/>
    <polygon points="300,108 340,108 340,130" fill="var(--slate-dark)"/>
    <rect x="300" y="46" width="360" height="62" fill="var(--slate)"/>
  </svg>

  <div class="wordmark"><span class="wordmark-square"></span>CEDAR RIDGE</div>

  <div class="name-ribbon">
    <div class="person-name">Carl Whitby</div>
    <div class="person-title">CMCA</div>
  </div>

  <ul class="contact-list">
    <li>
      <svg class="contact-icon" viewBox="0 0 24 24"><rect width="24" height="24" fill="var(--slate)"/><path d="M8 6l3 3-1.6 1.8c.9 1.8 2 2.9 3.8 3.8L15 13l3 3-2 2c-5 0-10-5-10-10z" fill="var(--white)"/></svg>
      541-327-4489
    </li>
    <li>
      <svg class="contact-icon" viewBox="0 0 24 24"><rect width="24" height="24" fill="var(--slate)"/><path d="M5 12l14-6-4 13-3-5z" fill="var(--white)"/></svg>
      541-327-6051
    </li>
    <li>
      <svg class="contact-icon" viewBox="0 0 24 24"><rect width="24" height="24" fill="var(--slate)"/><rect x="5" y="7" width="14" height="10" fill="none" stroke="var(--white)" stroke-width="1.6"/><path d="M5 7l7 6 7-6" fill="none" stroke="var(--white)" stroke-width="1.6"/></svg>
      info@cedarridgepg.com
    </li>
    <li>
      <svg class="contact-icon" viewBox="0 0 24 24"><rect width="24" height="24" fill="var(--slate)"/><circle cx="12" cy="12" r="6.5" fill="none" stroke="var(--white)" stroke-width="1.5"/><ellipse cx="12" cy="12" rx="2.8" ry="6.5" fill="none" stroke="var(--white)" stroke-width="1.2"/><line x1="5.5" y1="12" x2="18.5" y2="12" stroke="var(--white)" stroke-width="1.2"/></svg>
      www.cedarridgepg.com
    </li>
  </ul>

  <div class="address">
    <svg width="14" height="18" viewBox="0 0 14 18"><path d="M7 0a7 7 0 0 1 7 7c0 5-7 11-7 11S0 12 0 7a7 7 0 0 1 7-7z" fill="var(--white)"/><circle cx="7" cy="7" r="2.5" fill="var(--teal)"/></svg>
    812 NE Willow Ln., Suite 9<br>Bend, Oregon 97815
  </div>
</section>

</body>
</html>
```